Web site for Velmo Steadfast Advisory Pty. Ltd.

Create a modern website that is contemporary and appropriate for a business that is a provider of Consulting services to businesses. The LOGO is provided below. The consulting services offered are Supply Chain Management, 4th Party Logistics, Sales Coaching and training, HR services and training (i.e. Sexual Harassment and Bullying policies etc. ) , OH&S Training, Management mentoring, Business strategy and tactical consultations and Union related contract negotiations with award inclusion.

Target Market(s)

Importers, Exporters, Manufacturers, Freight Forwarders, Companies with large sales teams, warehouse operators

Industry/Entity Type

Business

Coding

Number of Pages Required

5+ page

Font styles to use
Serif
Sans Serif

Colors

Designer to choose colors to be used in the design.

Requirements
Must have
• Sky Line Photographs of Sydney and Manhattan, Pictures of people and teams in professional settings with tasteful clothing. Elements of both femininity and masculinity. People photos need to be diverse and include multiple nationalities, races and genders. Must have blog spot and also include the background info of the owners. Connectra pages includes.
Nice to have
• Would like to try both color and / or black and white.
Should not have
• Open

```html
<!DOCTYPE html>
<html lang="en">
<head>
<meta charset="utf-8">
<title>Velmo Steadfast Advisory</title>
<link href="https://fonts.googleapis.com/css2?family=Montserrat:wght@400;500;600;700&family=Open+Sans:wght@400;600&family=Poppins:wght@300;400;500&display=swap" rel="stylesheet">
<style>
:root{
  --ink:#1f1f1f;
  --text:#555;
  --muted:#888;
  --line:#e2e2e2;
  --paper:#fff;
  --soft:#f2f2f4;
  --grey:#efefef;
  --dark:#232323;
  --footer:#222222;
  --tab:#4a4a4a;
  --navy:#233b7a;
  --gold:#f1b500;
}
*{margin:0;padding:0;box-sizing:border-box}
html,body{width:1200px;height:2830px;overflow:hidden}
body{position:relative;background:var(--paper);font-family:"Open Sans",sans-serif;color:var(--text)}

/* header */
.header{position:absolute;left:0;top:0;width:1200px;height:128px;background:var(--paper)}
.brand{position:absolute;left:90px;top:28px;display:flex;align-items:center;gap:10px}
.brand-mark{width:14px;height:14px;background:var(--ink)}
.brand-name{font-family:"Montserrat",sans-serif;font-weight:600;font-size:30px;color:var(--ink);line-height:1}
.brand-tag{position:absolute;left:114px;top:72px;font-family:"Montserrat",sans-serif;font-weight:600;font-size:10px;color:var(--ink);letter-spacing:.3px}
.contact{position:absolute;top:30px;display:flex;gap:14px;align-items:center;font-family:"Poppins",sans-serif;font-size:12px;line-height:20px}
.contact b{display:block;font-weight:500;color:var(--ink)}
.contact span{color:var(--muted);font-size:13px}
.nav{position:absolute;top:89px;left:376px;display:flex;font-family:"Montserrat",sans-serif;font-weight:600;font-size:11.5px;color:var(--ink)}
.nav a{display:block;padding:0 15px;height:30px;line-height:30px;text-decoration:none;color:inherit;margin-right:9px}
.nav a.active{background:var(--ink);color:#fff}

/* hero */
.hero{position:absolute;left:0;top:128px;width:1200px;height:548px;background:linear-gradient(180deg,#3b3a3a 0%,#6b6358 45%,#2e2c2a 72%,#141414 100%)}
.hero-title{position:absolute;left:90px;top:182px;font-family:"Montserrat",sans-serif;color:#fff;font-size:47px;line-height:57px;font-weight:400}
.hero-title b{font-weight:700}

/* welcome */
.welcome{position:absolute;left:0;top:676px;width:1200px;height:636px;background:var(--soft)}
.welcome-title{position:absolute;left:100px;top:74px;width:288px;text-align:right;font-family:"Poppins",sans-serif;font-weight:400;font-size:23px;line-height:31px;color:var(--ink);letter-spacing:-.5px}
.welcome-rule{position:absolute;left:422px;top:80px;width:4px;height:56px;background:#777}
.welcome-text{position:absolute;left:452px;top:72px;width:640px;font-size:13px;line-height:23px;color:var(--text)}

.service{position:absolute;width:490px;height:162px}
.service .box{position:absolute;left:114px;top:0;right:0;bottom:0;background:var(--paper);border:1px solid var(--line);padding:26px 22px 0 53px}
.service.dark .box{background:var(--dark);border-color:var(--dark)}
.service .photo{position:absolute;left:0;top:16px;width:144px;height:134px;background:var(--paper);padding:7px;box-shadow:0 2px 8px rgba(0,0,0,.15)}
.service .photo div{width:100%;height:100%}
.service h3{font-family:"Open Sans",sans-serif;font-weight:600;font-size:18px;color:var(--ink);margin-bottom:10px;letter-spacing:.2px;white-space:nowrap}
.service p{font-size:12.5px;line-height:20px;color:var(--text)}
.service.dark h3,.service.dark p{color:#fff}

/* band */
.band{position:absolute;left:0;top:1312px;width:1200px;height:282px;background:linear-gradient(180deg,#3d3935 0%,#57514b 50%,#37332f 100%)}
.band h2{position:absolute;left:0;width:1200px;top:68px;text-align:center;font-family:"Montserrat",sans-serif;font-weight:700;font-size:33px;color:#fff}
.band p{position:absolute;left:0;width:1200px;top:116px;text-align:center;font-family:"Open Sans",sans-serif;font-weight:600;font-size:18px;color:#fff}
.tabs{position:absolute;top:1538px;left:366px;display:flex;gap:9px}
.tab{width:151px;height:56px;line-height:60px;text-align:center;font-family:"Montserrat",sans-serif;font-weight:600;font-size:17px;color:#fff;background:var(--tab)}
.tab.active{background:var(--paper);color:var(--navy)}
.tab:nth-child(2){width:144px}
.tab:nth-child(3){width:147px}

/* process */
.process-img{position:absolute;left:87px;top:1680px;width:238px;height:246px;background:linear-gradient(135deg,#e9e9e6 0%,#bfc3c4 50%,#8a8f92 100%)}
.section-head{font-family:"Montserrat",sans-serif;font-size:25px;color:#c8c8c8;font-weight:400}
.section-head b{color:var(--ink);font-weight:700}
.process{position:absolute;left:349px;top:1676px;width:420px}
.process p{margin-top:20px;font-family:"Poppins",sans-serif;font-size:12.5px;line-height:24px;color:var(--muted)}
.read-more{position:absolute;left:349px;top:1846px;width:158px;height:44px;border:3px solid var(--ink);font-family:"Poppins",sans-serif;font-size:13px;color:var(--ink);line-height:38px;padding-left:28px}
.read-more::after{content:"";position:absolute;right:-12px;top:-12px;width:18px;height:18px;border-top:3px solid var(--ink);border-right:3px solid var(--ink)}
.divider{position:absolute;left:821px;top:1684px;width:1px;height:240px;background:var(--line)}
.topics{position:absolute;left:877px;top:1676px;width:238px}
.topics ul{list-style:none;margin-top:14px}
.topics li{font-family:"Poppins",sans-serif;font-size:12px;color:var(--muted);height:40px;line-height:40px;border-bottom:1px solid var(--line);display:flex;align-items:center;gap:12px}
.topics li:last-child{border-bottom:0}

/* testimonial */
.testimonial{position:absolute;left:0;top:2015px;width:1200px;height:468px;background:var(--grey)}
.quote-mark{position:absolute;left:568px;top:52px}
.testimonial h2{position:absolute;left:0;width:1200px;top:100px;text-align:center;font-family:"Montserrat",sans-serif;font-weight:600;font-size:29px;color:var(--ink)}
.testimonial .quote{position:absolute;left:150px;width:900px;top:152px;text-align:center;font-family:"Poppins",sans-serif;font-size:15px;line-height:25px;color:var(--text)}
.avatars{position:absolute;top:2277px;left:0;width:1200px;display:flex;justify-content:center;align-items:center;gap:22px}
.avatar{border-radius:50%;border:3px solid #fff}
.person{position:absolute;left:0;width:1200px;top:2368px;text-align:center;font-family:"Montserrat",sans-serif}
.person b{display:block;font-size:14px;color:var(--ink);font-weight:700}
.stars{display:flex;justify-content:center;margin:4px 0 6px}
.person span{font-size:11px;color:var(--muted);font-family:"Open Sans",sans-serif}

/* footer */
.footer{position:absolute;left:0;top:2483px;width:1200px;height:347px;background:var(--footer);color:#ccc}
.footer h4{font-family:"Montserrat",sans-serif;font-weight:700;font-size:13px;color:#fff}
.f-brand{position:absolute;left:122px;top:30px;display:flex;align-items:center;gap:8px}
.f-brand .brand-name{color:#fff;font-size:24px}
.f-brand .brand-mark{background:#fff;width:11px;height:11px}
.f-tag{position:absolute;left:140px;top:64px;font-family:"Montserrat",sans-serif;font-size:8.5px;color:#fff;font-weight:600}
.f-about{position:absolute;left:102px;top:92px;width:230px;font-size:11.5px;line-height:20px;color:#ddd}
.f-contact{position:absolute;left:102px;top:180px;font-size:11.5px;line-height:29px;color:#ddd}
.f-contact div{display:flex;align-items:center;gap:9px}
.links{position:absolute;left:358px;top:72px;width:220px}
.links ul{list-style:none;display:grid;grid-template-columns:118px 100px;margin-top:14px}
.links li{font-size:11.5px;height:33px;line-height:33px;color:#ddd}
.news{position:absolute;left:613px;top:72px;width:210px}
.news .item{margin-top:18px}
.news .item b{display:block;font-weight:600;font-size:12px;line-height:20px;color:#fff}
.news .item span{font-size:10px;color:#888;display:flex;gap:7px;align-items:center;margin-top:6px}
.newsletter{position:absolute;left:872px;top:72px;width:232px}
.newsletter p{margin-top:16px;font-size:11.5px;line-height:20px;color:#ddd}
.newsletter .field{margin-top:26px;height:34px;background:#3a3a3a;text-align:center;line-height:34px;font-size:11px;color:#ccc}
.newsletter .btn{margin-top:4px;height:34px;background:#8a8a8a;text-align:center;line-height:34px;font-size:11px;font-weight:600;color:#222;letter-spacing:.5px}
.f-rule{position:absolute;left:102px;top:294px;width:1000px;height:1px;background:#3a3a3a}
.copyright{position:absolute;left:0;width:1200px;top:312px;text-align:center;font-size:11.5px;color:#ccc}
</style>
</head>
<body>

<header class="header">
  <div class="brand"><div class="brand-mark"></div><div class="brand-name">Velmo</div></div>
  <div class="brand-tag">Steadfast Advisory</div>

  <div class="contact" style="left:716px">
    <svg width="28" height="26" viewBox="0 0 28 26" fill="none" stroke="#666" stroke-width="1.6"><path d="M6 3l5 1 1 5-3 2c1.5 3 4 5.5 7 7l2-3 5 1 1 5c-10 1-19-8-18-18z"/></svg>
    <div><b>Call Us on</b><span>1-800-555-0143</span></div>
  </div>
  <div class="contact" style="left:908px">
    <svg width="34" height="24" viewBox="0 0 34 24" fill="none" stroke="#666" stroke-width="1.6"><rect x="7" y="4" width="24" height="16"/><path d="M7 4l12 9 12-9"/><path d="M1 9h5M2 14h4"/></svg>
    <div><b>Mail Us @</b><span>hello@velmoadvisory.com</span></div>
  </div>

  <nav class="nav">
    <a class="active">HOME</a><a>ABOUT</a><a>BUSINESS ADVISORY / CONSULTING</a><a>SKILLS TESTING</a><a>NEWS &amp; VIEWS</a><a style="margin-right:0">CONTACT</a>
  </nav>
</header>

<section class="hero" role="img" aria-label="Business people silhouetted against tall office windows overlooking a city skyline">
  <h1 class="hero-title"><b>Expert</b> in<br>Business <b>Advice</b></h1>
</section>

<section class="welcome">
  <h2 class="welcome-title">Welcome to Velmo<br>Top Consulting Agency</h2>
  <div class="welcome-rule"></div>
  <p class="welcome-text">Established in 2004 Corvale Performance Group which has been providing world class reliable advisory services and a host of complete business solutions for almost all the leading corporate as well as government organizations.</p>

  <div class="service dark" style="left:102px;top:196px">
    <div class="box"><h3>SUPPLY CHAIN &amp; 4PL LOGISTICS</h3><p>We streamline supply chains for importers, exporters and freight forwarders, and run fourth party logistics that keep goods moving.</p></div>
    <div class="photo"><div role="img" aria-label="Colleagues planning logistics at a laptop" style="background:linear-gradient(135deg,#c89a78,#8b4a36 60%,#5a2d25)"></div></div>
  </div>
  <div class="service" style="left:615px;top:196px">
    <div class="box"><h3>HR &amp; OH&amp;S TRAINING</h3><p>We write clear harassment and bullying policies and deliver safety training that protects your people on site.</p></div>
    <div class="photo"><div role="img" aria-label="Hands reviewing policy paperwork beside a laptop" style="background:linear-gradient(135deg,#efe6e6,#b99aa2 55%,#6c5057)"></div></div>
  </div>
  <div class="service" style="left:102px;top:392px">
    <div class="box"><h3>SALES COACHING</h3><p>Large sales teams sharpen their skills with practical coaching, training and mentoring that lifts results from week one.</p></div>
    <div class="photo"><div role="img" aria-label="Smiling sales coach in a blue shirt at a desk" style="background:linear-gradient(135deg,#dfe6ea,#7f9cb6 55%,#4d6680)"></div></div>
  </div>
  <div class="service" style="left:615px;top:392px">
    <div class="box"><h3>STRATEGY &amp; NEGOTIATION</h3><p>Strategy and tactical consults, management mentoring and union contract talks with award inclusion handled with care.</p></div>
    <div class="photo"><div role="img" aria-label="Consultant in glasses reviewing a contract" style="background:linear-gradient(135deg,#e8e6e3,#a39c95 55%,#5e5852)"></div></div>
  </div>
</section>

<section class="band" role="img" aria-label="Busy team meeting in a modern open-plan office">
  <h2>Reach for the Sky</h2>
  <p>– We know the language of business –</p>
</section>
<div class="tabs"><div class="tab active">Technology</div><div class="tab">Innovation</div><div class="tab">Integration</div></div>

<div class="process-img" role="img" aria-label="Overhead view of a team meeting around a white table"></div>
<div class="process">
  <h2 class="section-head">Creative <b>Process</b></h2>
  <p>Unlike other Frameworks which try to cover everything, it has been built specifically for modern teams. Aliquam sapien est, mollis id mattis id, scelerisque sed dolor. Proin accumsan erat sem, id porta risus dignissim ac.</p>
</div>
<div class="read-more">Read More &nbsp;→</div>
<div class="divider"></div>
<div class="topics">
  <h2 class="section-head">Useful <b>Topics</b></h2>
  <ul>
    <li><svg width="12" height="8" viewBox="0 0 12 8" fill="none" stroke="#444" stroke-width="1.4"><path d="M0 4h10M7 1l3 3-3 3"/></svg>The Best Creative business</li>
    <li><svg width="12" height="8" viewBox="0 0 12 8" fill="none" stroke="#444" stroke-width="1.4"><path d="M0 4h10M7 1l3 3-3 3"/></svg>Make more from your job</li>
    <li><svg width="12" height="8" viewBox="0 0 12 8" fill="none" stroke="#444" stroke-width="1.4"><path d="M0 4h10M7 1l3 3-3 3"/></svg>Money and Career</li>
    <li><svg width="12" height="8" viewBox="0 0 12 8" fill="none" stroke="#444" stroke-width="1.4"><path d="M0 4h10M7 1l3 3-3 3"/></svg>Get your Clarifications</li>
    <li><svg width="12" height="8" viewBox="0 0 12 8" fill="none" stroke="#444" stroke-width="1.4"><path d="M0 4h10M7 1l3 3-3 3"/></svg>Make the best of Everything</li>
  </ul>
</div>

<section class="testimonial">
  <svg class="quote-mark" width="64" height="30" viewBox="0 0 64 30" fill="#7a7a7a"><path d="M22 4c-7 2-11 7-11 14a6 6 0 1 0 6-6c0-3 2-5 6-6zM40 4c-7 2-11 7-11 14a6 6 0 1 0 6-6c0-3 2-5 6-6z"/></svg>
  <h2>2000+ Choice Client</h2>
  <p class="quote">" We worked with Brightmere. Our representative was very knowledgeable and helpful. Brightmere made a number of suggestions to help improve our systems. Brightmere explained how things work and why it would help. We are pleased with the result and we definitely highly recommend Brightmere."</p>
</section>
<div class="avatars">
  <div class="avatar" style="width:52px;height:52px;background:radial-gradient(circle at 50% 40%,#f1d9b8,#c9a67a)" role="img" aria-label="Client portrait"></div>
  <div class="avatar" style="width:72px;height:72px;background:radial-gradient(circle at 50% 40%,#c7b3a0,#233b63)" role="img" aria-label="Client portrait"></div>
  <div class="avatar" style="width:52px;height:52px;background:radial-gradient(circle at 50% 40%,#e2e2e2,#6d6d6d)" role="img" aria-label="Client portrait"></div>
</div>
<div class="person">
  <b>Dana Whitlock</b>
  <div class="stars">
    <svg width="60" height="11" viewBox="0 0 60 11" fill="var(--gold)"><g id="s"><path d="M5.5 0l1.6 3.6 3.9.3-3 2.5 1 3.8-3.5-2.1-3.5 2.1 1-3.8-3-2.5 3.9-.3z"/></g><use href="#s" x="12"/><use href="#s" x="24"/><use href="#s" x="36"/><use href="#s" x="48"/></svg>
  </div>
  <span>CEO Fernbrook Studio</span>
</div>

<footer class="footer">
  <div class="f-brand"><div class="brand-mark"></div><div class="brand-name">Velmo</div></div>
  <div class="f-tag">Steadfast Advisory</div>
  <p class="f-about">Lorem ipsum dolor sit amet, consectetur adipisicing elit, sed do eiusmod tempor incididunt ut labore</p>
  <div class="f-contact">
    <div><svg width="10" height="13" viewBox="0 0 10 13" fill="#ccc"><path d="M5 0a5 5 0 0 0-5 5c0 4 5 8 5 8s5-4 5-8a5 5 0 0 0-5-5zm0 7a2 2 0 1 1 0-4 2 2 0 0 1 0 4z"/></svg>12 Harbour Lane, Sydney, AU</div>
    <div><svg width="11" height="11" viewBox="0 0 11 11" fill="#ccc"><path d="M2 0l2 .5.5 2.5-1.3 1c.7 1.4 1.8 2.5 3.2 3.2l1-1.3 2.5.5L10 9.5C5 10 0 5 .5 0z"/></svg>001-555-0199</div>
    <div><svg width="12" height="9" viewBox="0 0 12 9" fill="none" stroke="#ccc" stroke-width="1.3"><rect x=".5" y=".5" width="11" height="8"/><path d="M.5.5l5.5 4 5.5-4"/></svg>info@velmoadvisory.com</div>
  </div>

  <div class="links">
    <h4>Our Links</h4>
    <ul>
      <li>»&nbsp; Home</li><li>»&nbsp; News</li>
      <li>»&nbsp; About Us</li><li>»&nbsp; Shop</li>
      <li>»&nbsp; Services</li><li>»&nbsp; Contact</li>
      <li>»&nbsp; Pages</li><li>»&nbsp; Support</li>
      <li>»&nbsp; Projects</li><li>»&nbsp; Careers</li>
    </ul>
  </div>

  <div class="news">
    <h4>Recent News</h4>
    <div class="item"><b>Colombia Gets a Business Makeover</b><span><svg width="10" height="10" viewBox="0 0 10 10" fill="none" stroke="#888" stroke-width="1.2"><circle cx="5" cy="5" r="4.3"/><path d="M5 2.5V5h2"/></svg>20 AUG 2017</span></div>
    <div class="item"><b>Counting the Cost of Delay &amp; Disruption</b><span><svg width="10" height="10" viewBox="0 0 10 10" fill="none" stroke="#888" stroke-width="1.2"><circle cx="5" cy="5" r="4.3"/><path d="M5 2.5V5h2"/></svg>20 AUG 2017</span></div>
  </div>

  <div class="newsletter">
    <h4>Newsletter</h4>
    <p>Subscribe our newsletter gor get noti-fication about new updates, etc.</p>
    <div class="field">Enter Your Email</div>
    <div class="btn">SUBSCRIBE</div>
  </div>

  <div class="f-rule"></div>
  <p class="copyright">Copyright @2018 Velmo Steadfast Advisory. All rights reserved.</p>
</footer>

</body>
</html>
```